Retractable Banner Design for Willowbrook Critters Florida Rebrand

We need a retractable banner design for our market booth. I absolutely love our old banner design and would like to keep it clean and similar but more on theme with the new brand with the new colors. Full brand guide attached. Our slogan we would like to include is "professional pet care for when you can't be there" (dog walking & pet sitting).
Our services we would like to include is: Extended Visits, Pop In Visits, Dog Walking, Pet Taxi, Travel & Adventure Hikes.
We offer: Discounts for First Responders, Teachers, & Military
I would like to use elements from the brand as well as the colors. Include the website www.willowbrookcritters.net somewhere

```html
<!DOCTYPE html>
<html lang="en">
<head>
<meta charset="utf-8">
<title>Willowbrook Critters Florida – Retractable Banner</title>
<link href="https://fonts.googleapis.com/css2?family=Fraunces:opsz,wght@9..144,800;9..144,900&family=Poppins:wght@500;600;700&display=swap" rel="stylesheet">
<style>
  :root {
    --magenta: #d43891;
    --teal: #134b5a;
    --gold: #e9c166;
    --cream: #fbf0dc;
    --white: #ffffff;
    --stage: #eef0ef;
  }
  * { margin: 0; padding: 0; box-sizing: border-box; }
  html, body { width: 736px; height: 1200px; overflow: hidden; background: var(--stage); }
  .banner {
    position: absolute; left: 128px; top: 0;
    width: 480px; height: 1200px;
    background: var(--magenta); overflow: hidden;
    font-family: "Poppins", sans-serif;
  }
  .backdrop { position: absolute; inset: 0; }
  .brand-name {
    position: absolute; top: 48px; left: 0; width: 480px;
    text-align: center; color: var(--teal);
    font-family: "Fraunces", serif; font-weight: 900;
    font-size: 40px; line-height: 1.05;
  }
  .headline {
    position: absolute; top: 302px; left: 0; width: 480px;
    text-align: center; color: var(--cream);
    font-family: "Fraunces", serif; font-weight: 800;
    font-size: 48px; line-height: 1.1; letter-spacing: 0.3px;
  }
  .headline-pill {
    position: absolute; top: 367px; left: 99px; width: 282px; height: 55px;
    background: var(--gold); border-radius: 28px;
    color: var(--teal); font-family: "Fraunces", serif; font-weight: 900;
    font-size: 38px; line-height: 55px; text-align: center;
  }
  .tagline {
    position: absolute; top: 430px; left: 0; width: 480px;
    text-align: center; color: var(--cream);
    font-weight: 600; font-size: 22px; letter-spacing: 0.9px;
  }
  .team-photo {
    position: absolute; width: 138px; height: 138px; border-radius: 50%;
    border: 6px solid var(--white);
    box-shadow: 0 4px 10px rgba(0,0,0,0.25);
  }
  .team-photo.one { left: 15px; top: 482px; background: linear-gradient(160deg, #b9c8cf 0%, #8d9a6a 35%, #3a3a30 70%, #5b3b24 100%); }
  .team-photo.two { left: 175px; top: 485px; background: linear-gradient(180deg, #4c5e35 0%, #2e3228 45%, #a48f78 70%, #6f8f3e 100%); }
  .team-photo.three { left: 327px; top: 525px; background: linear-gradient(180deg, #9fbcd6 0%, #dbe4ea 38%, #3c4350 60%, #6a6d70 100%); }
  .services {
    position: absolute; left: 35px; top: 698px; width: 410px; height: 232px;
    border: 3px solid var(--gold); border-radius: 22px; background: var(--white);
  }
  .services-label {
    position: absolute; left: 113px; top: 679px; width: 254px; height: 40px;
    background: var(--magenta); border-radius: 20px;
    color: var(--white); font-weight: 700; font-size: 21px;
    line-height: 40px; text-align: center; letter-spacing: 0.3px;
  }
  .service { position: absolute; width: 130px; text-align: center; color: var(--teal); font-weight: 500; font-size: 13px; line-height: 1.3; }
  .service svg { display: block; margin: 0 auto 4px; }
  .service.extended { left: 59px; top: 732px; }
  .service.popin { left: 181px; top: 732px; }
  .service.walking { left: 303px; top: 732px; }
  .service.taxi { left: 116px; top: 828px; }
  .service.travel { left: 244px; top: 822px; }
  .pets-photo {
    position: absolute; left: 0; top: 935px; width: 480px; height: 172px;
    background:
      linear-gradient(180deg, rgba(255,255,255,1) 0%, rgba(255,255,255,0) 45%),
      linear-gradient(90deg, #e6e3df 0%, #d9d4cf 14%, #c98f58 24%, #d49a5e 36%, #5a4333 50%, #8a6a4c 58%, #8a5a38 72%, #e9e7e4 88%, #f1efec 100%);
  }
  .offer {
    position: absolute; left: 84px; top: 1050px; width: 324px; height: 78px;
    background: var(--cream); border: 4px solid var(--magenta); border-radius: 39px;
    text-align: center;
  }
  .offer-title { margin-top: 5px; color: var(--magenta); font-family: "Fraunces", serif; font-weight: 900; font-size: 25px; line-height: 1; }
  .offer-text { margin-top: 3px; color: var(--teal); font-weight: 600; font-size: 14px; line-height: 1.3; }
  .website {
    position: absolute; top: 1142px; left: 0; width: 480px;
    text-align: center; color: var(--white); font-weight: 600; font-size: 26px;
  }
</style>
</head>
<body>
<main class="banner">
  <svg class="backdrop" width="480" height="1200" viewBox="0 0 480 1200" aria-hidden="true">
    <path d="M0 86 C60 190 150 217 240 217 C330 217 420 190 480 102 V0 H0 Z" fill="var(--white)"/>
    <path d="M0 122 C70 235 160 262 240 262 C320 262 410 238 480 160" fill="none" stroke="var(--white)" stroke-width="5"/>
    <path d="M0 130 C70 250 160 278 240 278 C320 278 410 252 480 172" fill="none" stroke="var(--gold)" stroke-width="13"/>
    <path d="M0 660 C80 600 160 578 240 578 C330 578 420 620 480 700 V1107 H0 Z" fill="var(--white)"/>
    <path d="M0 628 C80 560 160 538 240 538 C330 538 420 585 480 672" fill="none" stroke="var(--gold)" stroke-width="12"/>
    <path d="M0 642 C80 574 160 552 240 552 C330 552 420 598 480 684" fill="none" stroke="var(--white)" stroke-width="5"/>
  </svg>

  <h1 class="brand-name">Willowbrook<br>Critters Florida</h1>

  <h2 class="headline">PROFESSIONAL</h2>
  <div class="headline-pill">PET CARE</div>
  <p class="tagline">FOR WHEN YOU CAN'T BE THERE</p>

  <div class="team-photo one" role="img" aria-label="Pet sitter kneeling with a brown dog among beach plants"></div>
  <div class="team-photo two" role="img" aria-label="Two pet sitters crouching beside a dog on grass"></div>
  <div class="team-photo three" role="img" aria-label="Team with clients and small dogs on an airfield"></div>

  <section class="services"></section>
  <div class="services-label">OUR SERVICES</div>

  <div class="service extended">
    <svg width="64" height="54" viewBox="0 0 64 54" aria-hidden="true">
      <circle cx="28" cy="30" r="21" fill="none" stroke="var(--teal)" stroke-width="6"/>
      <path d="M28 17 V30 L21 38" fill="none" stroke="var(--magenta)" stroke-width="3" stroke-linecap="round"/>
      <circle cx="50" cy="12" r="10" fill="var(--magenta)" stroke="var(--white)" stroke-width="2"/>
      <path d="M50 7 V17 M45 12 H55" stroke="var(--white)" stroke-width="2.5"/>
    </svg>
    EXTENDED VISITS
  </div>
  <div class="service popin">
    <svg width="64" height="54" viewBox="0 0 64 54" aria-hidden="true">
      <rect x="24" y="4" width="22" height="48" fill="var(--teal)"/>
      <rect x="46" y="14" width="10" height="38" fill="var(--teal)"/>
      <g fill="var(--white)"><rect x="29" y="10" width="4" height="4"/><rect x="37" y="10" width="4" height="4"/><rect x="29" y="20" width="4" height="4"/><rect x="37" y="20" width="4" height="4"/><rect x="29" y="30" width="4" height="4"/><rect x="37" y="30" width="4" height="4"/></g>
      <path d="M18 52 C10 40 6 35 6 29 a12 12 0 0 1 24 0 c0 6 -4 11 -12 23Z" fill="var(--magenta)" stroke="var(--white)" stroke-width="2"/>
      <circle cx="18" cy="29" r="4" fill="var(--white)"/>
    </svg>
    POP IN VISITS
  </div>
  <div class="service walking">
    <svg width="64" height="54" viewBox="0 0 64 54" aria-hidden="true">
      <circle cx="20" cy="6" r="5" fill="var(--teal)"/>
      <path d="M20 14 L17 32 M17 32 L11 51 M17 32 L25 51 M19 18 L10 27 M19 18 L30 26" fill="none" stroke="var(--teal)" stroke-width="6" stroke-linecap="round"/>
      <path d="M30 26 L48 40" fill="none" stroke="var(--magenta)" stroke-width="1.5"/>
      <path d="M44 40 H56 L58 35 L60 38 V44 L58 51 H55 L54 46 H48 L47 51 H44 L44 44 L41 40 Z" fill="var(--magenta)"/>
    </svg>
    DOG WALKING
  </div>
  <div class="service taxi">
    <svg width="100" height="54" viewBox="0 0 100 54" aria-hidden="true">
      <path d="M4 30 H24 L34 16 H62 L74 30 H96 V44 H4 Z" fill="var(--teal)"/>
      <path d="M37 20 H47 V30 H30 Z M51 20 H60 L68 30 H51 Z" fill="var(--white)"/>
      <rect x="44" y="11" width="12" height="5" fill="var(--teal)"/>
      <circle cx="22" cy="46" r="7" fill="var(--magenta)" stroke="var(--white)" stroke-width="2"/>
      <circle cx="78" cy="46" r="7" fill="var(--magenta)" stroke="var(--white)" stroke-width="2"/>
      <circle cx="16" cy="14" r="12" fill="var(--magenta)"/>
      <g fill="var(--white)"><ellipse cx="16" cy="18" rx="4" ry="3.5"/><circle cx="11" cy="12" r="2"/><circle cx="15" cy="9" r="2"/><circle cx="19" cy="9" r="2"/><circle cx="22" cy="13" r="2"/></g>
    </svg>
    PET TAXI
  </div>
  <div class="service travel">
    <svg width="70" height="54" viewBox="0 0 70 54" aria-hidden="true">
      <circle cx="32" cy="24" r="21" fill="var(--teal)"/>
      <path d="M16 14 Q26 10 30 16 Q26 22 20 22 Z M36 8 Q46 10 48 20 Q40 22 36 16 Z" fill="var(--white)"/>
      <path d="M8 44 L40 34 L48 28 L52 31 L46 37 L38 41 L30 50 L26 49 L30 43 L14 47 Z" fill="var(--teal)" stroke="var(--white)" stroke-width="1.5"/>
      <path d="M50 30 Q58 22 64 30 L62 44 Q56 50 50 44 Z" fill="var(--magenta)"/>
    </svg>
    TRAVEL &amp;<br>ADVENTURE HIKES
  </div>

  <div class="pets-photo" role="img" aria-label="Row of rabbits, dogs and a cat sitting together on a white background"></div>

  <div class="offer">
    <p class="offer-title">WE OFFER</p>
    <p class="offer-text">Discounts for First Responders,<br>Teachers, &amp; Military</p>
  </div>

  <p class="website">www.willowbrookcritters.net</p>
</main>
</body>
</html>
```